Prairie Reading Alliance - Minds Unbound Website

We need a website designed for a PR + Marketing Campaign (Minds Unbound: Our Daily Craft) for the Prairie Reading Alliance (PRA), the largest statewide library association in the country.

The final design should communicate an empowerment to libraries, its innovative practices, and how they are helping and improving the lives of all communities (of all ages, backgrounds, experiences).

The look should be bold, captivating; meanwhile also simple, clean, easy-to-navigate.

LAYOUT (five pages total):
Page 1: Home – Intro
Animated logo transitioning into simple landing page.
Must feature #shelvesinmotion and eventually featuring video.

Page 2: About the Campaign
Graphics/photos optional, text below:
Broad Objectives and Goals
Minds Unbound: Our Daily Craft seeks to broaden the awareness of library services to the public and provide resources to librarians working in the state in order to promote libraries as vital, technology-centered institutions in the community.
The campaign provides a platform for the sharing of ideas and resources that strengthen the image of the library profession and the services provided by libraries in Texas.
Related goals include: providing librarians with the tools necessary to influence key supporters, shifting the perspectives of libraries as a center for books to a center for emerging technology and the cultivation of ideas, and spreading the message of the campaign through both traditional and social media outlets.
Librarians and information professionals are encouraged to actively participate in the campaign through social media outlets, using the hashtag #shelvesinmotion, and by contributing content in the Ideas Shared portion of the campaign website.

Page 3: Toolkit – downloadable items
Downloadable Campaign Materials for library professionals
Buttons leading to subpages or one large page covering the topics below

Page 4: Ideas Shared: What We Do: Interactive element page
Toolkit
Here are the tools and downloadable materials for #shelvesinmotion everywhere. Use these campaign designs to showcase the innovation happening in your library! Check back as we continue to update this page with new content.
Logos
Campaign logos in various formats for use on your own customized designs.
Print Materials
Flyers, bookmarks, posters and more!
Web & Interactive
Graphics for social media and the Web.
Coming soon: #shelvesinmotion campaign video!
PR & Marketing
Sample press releases, emails, and customizable content for a variety of library types: school, academic, public, and special.

Page 5: Contact Us Page
Can either be a sub-section of the About Us page, or a stand-alone link.
Standard submission form with the ability to upload documents for the Ideas Shared section.
Contact Us
Have a question or comment? Want to contribute a summary and photos or video of your innovative programs for the Ideas Shared section? Please get in touch!
NAME:
EMAIL:
PHONE:
ADDRESS: ?
MESSAGE:
ATTACHMENTS (upload)

MUST HAVE:
-Maintain the color-scheme of the logo (attached)
-The WEBSITE design must innovation and excitement. a contemporary design/layout that demonstrates vitality
-Somewhere on every page, we would like an interactive element for viewers, such as a stream from Chatterloop/Peepline with hashtags.
-Countdown to Campaign Launch
-Can we include animation? We are striving to create movement with the abstract icon in our log.

PLEASE AVOID:
-NO pastels, NO soft colors, nothing that might be considered feminine (pinks, etc); we do want to stear away from stereotypes (NO books, NO library buildings, NO reading conceptual designs) and standard icons (NO lightbulbs and NO lightning designs)

AUDIENCE/MARKET:
THE PUBLIC (also includes all kinds of librarians and their supporters: information, reference, school, public, special, law, academic, students, educators, administration, support staff, lay and advocates)

AUDIENCE/MARKET:

Requirements
Must have
• The final design should communicate an empowerment to libraries, its innovative practices, and how they are helping and improving the lives of all communities (of all ages, backgrounds, experiences).
• The look should be bold, captivating; meanwhile also simple, clean, easy-to-navigate.
• LAYOUT (five pages total):
• Page 1: Home – Intro
• Animated logo transitioning into simple landing page.
• Must feature #shelvesinmotion and eventually featuring video.
• Page 2: About the Campaign
• Graphics/photos optional, text below:
• Broad Objectives and Goals
• Minds Unbound: Our Daily Craft seeks to broaden the awareness of library services to the public and provide resources to librarians working in the state in order to promote libraries as vital, technology-centered institutions in the community.
• The campaign provides a platform for the sharing of ideas and resources that strengthen the image of the library profession and the services provided by libraries in Texas.
• Related goals include: providing librarians with the tools necessary to influence key supporters, shifting the perspectives of libraries as a center for books to a center for emerging technology and the cultivation of ideas, and spreading the message of the campaign through both traditional and social media outlets.
• Librarians and information professionals are encouraged to actively participate in the campaign through social media outlets, using the hashtag #shelvesinmotion, and by contributing content in the Ideas Shared portion of the campaign website.
• Page 3: Toolkit – downloadable items
• Downloadable Campaign Materials for library professionals
• Buttons leading to subpages or one large page covering the topics below
• Page 4: Ideas Shared: What We Do: Interactive element page
• Toolkit
• Here are the tools and downloadable materials for #shelvesinmotion everywhere. Use these campaign designs to showcase the innovation happening in your library! Check back as we continue to update this page with new content.
• Logos
• Campaign logos in various formats for use on your own customized designs.
• Print Materials
• Flyers, bookmarks, posters and more!
• Web & Interactive
• Graphics for social media and the Web.
• Coming soon: #shelvesinmotion campaign video!
• PR & Marketing
• Sample press releases, emails, and customizable content for a variety of library types: school, academic, public, and special.
• Page 5: Contact Us Page
• Can either be a sub-section of the About Us page, or a stand-alone link.
• Standard submission form with the ability to upload documents for the Ideas Shared section.
• Contact Us
• Have a question or comment? Want to contribute a summary and photos or video of your innovative programs for the Ideas Shared section? Please get in touch!
• NAME:
• EMAIL:
• PHONE:
• ADDRESS: ?
• MESSAGE:
• ATTACHMENTS (upload)
• MUST HAVE:
• -Maintain the color-scheme of the logo (attached)
• -The WEBSITE design must innovation and excitement. a contemporary design/layout that demonstrates vitality
• -Somewhere on every page, we would like an interactive element for viewers, such as a stream from Chatterloop/Peepline with hashtags.
• -Countdown to Campaign Launch
• -Can we include animation? We are striving to create movement with the abstract icon in our log.
Should not have
• PLEASE AVOID:
• -NO pastels, NO soft colors, nothing that might be considered feminine (pinks, etc); we do want to stear away from stereotypes (NO books, NO library buildings, NO reading conceptual designs) and standard icons (NO lightbulbs and NO lightning designs)

```html
<!DOCTYPE html>
<html lang="en">
<head>
<meta charset="utf-8">
<title>Minds Unbound – Prairie Reading Alliance</title>
<link href="https://fonts.googleapis.com/css2?family=Open+Sans:wght@300;400;600&display=swap" rel="stylesheet">
<style>
  :root{
    --brand:#2a9fd8;
    --ink:#333;
    --body:#555;
    --muted:#8a8a8a;
    --soft-bg:#f2f4f6;
    --footer:#1c1c1c;
    --footer-text:#a9a9a9;
  }
  *{box-sizing:border-box;margin:0;padding:0}
  html,body{width:1001px;height:1200px;overflow:hidden}
  body{font-family:"Open Sans",Arial,sans-serif;color:var(--ink);background:#fff;position:relative}
  .top-line{position:absolute;left:0;top:0;width:100%;height:3px;background:var(--brand)}
  .site-header{position:absolute;left:0;top:3px;width:100%;height:112px;background:#fff}
  .brand{position:absolute;left:82px;top:26px;display:flex;align-items:flex-start;gap:10px}
  .brand-mark{width:30px;height:30px;border:3px solid var(--brand);border-radius:4px;margin-top:2px}
  .brand-name{font-size:19px;font-weight:600;color:var(--brand);letter-spacing:.5px;line-height:22px}
  .brand-tagline{font-size:10px;letter-spacing:3px;color:#9a9a9a;text-transform:uppercase;margin-top:3px}
  .main-nav{position:absolute;top:0;left:0}
  .main-nav a{position:absolute;top:50px;font-size:12.5px;color:var(--muted);text-decoration:none;white-space:nowrap}
  .main-nav .is-active{left:430px;top:38px;width:50px;height:42px;border:3px solid var(--brand);border-radius:5px;color:var(--brand);display:flex;align-items:center;justify-content:center;transform:rotate(-3deg)}
  .hero{position:absolute;left:0;top:115px;width:100%;height:431px;
    background:radial-gradient(ellipse at 50% 60%,#2d5f84 0%,#173f66 45%,#0c2947 100%);
    text-align:center;color:#fff}
  .hero h1{position:absolute;top:134px;width:100%;font-size:37px;font-weight:400;letter-spacing:.5px}
  .hero p{position:absolute;top:194px;left:150px;width:701px;font-size:16px;line-height:25px}
  .login{position:absolute;top:276px;width:128px;height:25px;font-size:10px;color:#fff;display:flex;align-items:center;gap:8px;padding-left:4px;border-radius:2px}
  .login .dot{width:17px;height:17px;border-radius:50%;background:rgba(255,255,255,.35)}
  .login--chatter{left:368px;background:#2f69b3}
  .login--peep{left:504px;background:#31a7df}
  .welcome{position:absolute;left:0;top:546px;width:100%;height:291px;background:var(--soft-bg);border-bottom:1px solid #e3e6e9}
  .welcome h2{position:absolute;left:82px;top:42px;font-size:22px;font-weight:400;color:#333}
  .welcome h2 span{color:var(--brand)}
  .welcome .lead{position:absolute;left:82px;top:92px;width:473px;font-size:10px;line-height:17.2px;color:var(--body);text-align:justify}
  .welcome .more{position:absolute;left:82px;top:226px;font-size:13px;color:var(--brand);text-decoration:none}
  .video-frame{position:absolute;left:598px;top:46px;width:320px;height:188px;background:#fff;padding:4px;box-shadow:0 0 3px rgba(0,0,0,.15)}
  .video-still{width:100%;height:100%;background:linear-gradient(135deg,#5a4631 0%,#8c6c4b 45%,#6f7d8c 75%,#c9b79d 100%);position:relative}
  .play{position:absolute;left:50%;top:50%;width:0;height:0;margin:-10px 0 0 -6px;border-left:18px solid #222;border-top:10px solid transparent;border-bottom:10px solid transparent}
  .contact-strip{position:absolute;left:0;top:837px;width:100%;height:161px;background:#fff}
  .contact-item{position:absolute;top:47px}
  .contact-icon{position:absolute;left:0;top:0;width:59px;height:59px;border-radius:50%;background:var(--brand);border:3px solid #eef0f2;box-shadow:0 1px 3px rgba(0,0,0,.15);display:flex;align-items:center;justify-content:center}
  .contact-item h3{position:absolute;top:0;font-size:15px;font-weight:400;color:var(--brand);white-space:nowrap}
  .contact-item p{position:absolute;top:26px;font-size:10px;line-height:17px;color:var(--body);white-space:nowrap}
  .site-footer{position:absolute;left:0;top:998px;width:100%;height:202px;background:var(--footer);color:var(--footer-text)}
  .footer-nav{position:absolute;left:85px;top:44px;font-size:9.5px}
  .footer-nav span{margin:0 7px;color:#777}
  .copyright{position:absolute;left:85px;top:66px;font-size:9.5px}
  .footer-brand{position:absolute;left:85px;top:96px}
  .footer-brand .brand-name{color:#9a9a9a;font-size:15px}
  .footer-brand .brand-tagline{color:#777;font-size:8px;letter-spacing:2.5px}
  .social{position:absolute;left:808px;top:50px;display:flex;gap:6px}
  .social i{display:block;width:23px;height:23px;border-radius:50%;background:#3a7fc0}
  .partner{position:absolute;left:848px;top:94px;font-size:24px;font-weight:600;color:#9a9a9a;letter-spacing:1px}
</style>
</head>
<body>
  <div class="top-line"></div>

  <header class="site-header">
    <div class="brand">
      <div class="brand-mark"></div>
      <div>
        <div class="brand-name">Minds Unbound</div>
        <div class="brand-tagline">Our Daily Craft</div>
      </div>
    </div>
    <nav class="main-nav">
      <a class="is-active" href="#">Home</a>
      <a href="#" style="left:515px">About the Campaign</a>
      <a href="#" style="left:669px">Toolkit</a>
      <a href="#" style="left:750px">Ideas shared</a>
      <a href="#" style="left:862px">Contact us</a>
    </nav>
  </header>

  <section class="hero" role="img" aria-label="Dark blue photo backdrop of an open book with faint binary digits and hexagon shapes">
    <h1>Shelves in Motion</h1>
    <p>2015-2016 Prairie Reading Alliance President Dana Whitfield charged the PRA PR &amp; Marketing committee with the task of creating a big campaign to raise awareness about...</p>
    <a class="login login--chatter"><span class="dot"></span>Login with Chatterloop</a>
    <a class="login login--peep"><span class="dot"></span>Login with Peepline</a>
  </section>

  <section class="welcome">
    <h2>Welcome to <span>Rookvault</span></h2>
    <p class="lead">Perspiciatis unde omnis iste natus error sit voluptatem accusantium doloremque laudantium, totam rem aperiam, eaque ipsa quae ab illo inventore veritatis et quasi architecto beatae vitae dicta sunt explicabo. Nemo enim ipsam voluptatem quia voluptas sit aspernatur aut odit aut fugit, sed quia consequuntur magni dolores eos qui ratione voluptatem sequi nesciunt. Neque porro quisquam est, qui dolorem ipsum quia dolor sit amet, consectetur, adipisci velit, sed quia non numquam eius modi tempora incidunt ut labore et dolore magnam aliquam quaerat voluptatem. Ut enim ad minima veniam, quis nostrum exercitationem ullam corporis suscipit laboriosam,</p>
    <a class="more" href="#">Read More</a>
    <div class="video-frame">
      <div class="video-still" role="img" aria-label="Video still of three students studying together with a tablet in a library">
        <span class="play"></span>
      </div>
    </div>
  </section>

  <section class="contact-strip">
    <div class="contact-item" style="left:82px">
      <div class="contact-icon">
        <svg width="14" height="18" viewBox="0 0 14 18"><path d="M7 0C3.1 0 0 3 0 6.8 0 11.5 7 18 7 18s7-6.5 7-11.2C14 3 10.9 0 7 0zm0 9.3a2.5 2.5 0 1 1 0-5 2.5 2.5 0 0 1 0 5z" fill="#fff"/></svg>
      </div>
      <h3 style="left:83px">Address</h3>
      <p style="left:80px">200 Latin words, combined with a handful of<br>model sentence structures</p>
    </div>
    <div class="contact-item" style="left:438px">
      <div class="contact-icon">
        <svg width="17" height="17" viewBox="0 0 24 24"><path d="M6.6 10.8a15.1 15.1 0 0 0 6.6 6.6l2.2-2.2c.3-.3.7-.4 1-.2 1.1.4 2.3.6 3.6.6.6 0 1 .4 1 1V20c0 .6-.4 1-1 1A17 17 0 0 1 3 4c0-.6.4-1 1-1h3.5c.6 0 1 .4 1 1 0 1.3.2 2.5.6 3.6.1.3 0 .7-.2 1z" fill="#fff"/></svg>
      </div>
      <h3 style="left:80px">Call Us On</h3>
      <p style="left:77px;top:29px">+ 0100555014 / 0100555018</p>
    </div>
    <div class="contact-item" style="left:731px">
      <div class="contact-icon">
        <svg width="20" height="15" viewBox="0 0 20 15"><rect x="1" y="1" width="18" height="13" rx="1.5" fill="none" stroke="#fff" stroke-width="2"/><path d="M1.5 2l8.5 6.5L18.5 2" fill="none" stroke="#fff" stroke-width="2"/></svg>
      </div>
      <h3 style="left:75px">Mail Us</h3>
      <p style="left:75px">info@mindsunbound.example</p>
    </div>
  </section>

  <footer class="site-footer">
    <div class="footer-nav">Home<span>|</span>About the Campaign<span>|</span>Toolkit<span>|</span>Ideas shared<span>|</span>Contact us</div>
    <div class="copyright">Copyright &copy; 2015 Minds Unbound. &nbsp;All rights reserved.</div>
    <div class="footer-brand">
      <div class="brand-name">Minds Unbound</div>
      <div class="brand-tagline">Our Daily Craft</div>
    </div>
    <div class="social" aria-label="Social links"><i></i><i></i><i></i><i></i></div>
    <div class="partner">PRA</div>
  </footer>
</body>
</html>
```